Under Copper Lanterns to WANDERLAND - Practical notes on Arranging your garden, kitchen, and study.

PLEASE READ: My book is all about optimizing a person's health.
Most people go through life in pain, low energy, disappointed with their body and living a short life relying on medication. I call this "Surviving"

My Goal is to transform their life from serving to THRIVING. This is why you see the background I these images as a cold, dark cracking desert. From this cold dark desert I want there to be a thriving and emerging plant brain like the one seen on image #1. I also want my readers to pick up the book and know that the book is about humans. So I want there to be a nervous system like in image #2 Lastly on image 3. I want there to be consistency throughout the whole book. Like the cracking desert in the background of the back cover.

Target Market(s)

People struggling with their health

Industry/Entity Type

Health

Colors
0054AA
0677BA
7BADD7
CADEEF
E8F1F8
00AB8E
00BBA5
67D7C9
C6EFE9
E9F9F6

Requirements
Must have
• Brain, and Nervous system.
Nice to have
• Colors selected

```html
<!DOCTYPE html>
<html lang="en">
<head>
<meta charset="utf-8">
<title>Under Copper Lanterns to Wanderland — Book Jacket</title>
<link rel="stylesheet" href="https://fonts.googleapis.com/css2?family=Archivo+Black&family=Arimo:wght@400;700&display=swap">
<style>
  :root {
    --page-bg: #e8e8e8;
    --lime: #b0ff00;
    --white: #ffffff;
    --ink: #0a0a0a;
    --paper: #fffdf5;
    --sky-light: #9a9a9a;
    --sky-mid: #4a4a4a;
    --ground: #1c1c1a;
  }
  * { margin: 0; padding: 0; box-sizing: border-box; }
  html, body { width: 1200px; height: 1200px; overflow: hidden; background: var(--page-bg); }
  .jacket { position: relative; width: 1200px; height: 1200px; }

  .back-cover, .spine, .front-cover { position: absolute; overflow: hidden; }
  .back-cover { left: 36px; top: 189px; width: 506px; height: 758px; }
  .spine { left: 561px; top: 187px; width: 64px; height: 760px; }
  .front-cover { left: 642px; top: 186px; width: 506px; height: 761px; }

  .scene {
    position: absolute; inset: 0;
    background:
      linear-gradient(180deg, rgba(0,0,0,0.85) 0%, rgba(0,0,0,0) 8%),
      linear-gradient(180deg, #2a2a2a 0%, var(--sky-mid) 14%, var(--sky-light) 28%, #6b6b6b 36%, #161616 40%, #2c2c2a 60%, var(--ground) 85%, #060606 100%);
  }
  .scene--front::after {
    content: ""; position: absolute;
    left: 80px; top: 330px; width: 320px; height: 300px;
    background: radial-gradient(ellipse at 50% 45%, rgba(90,130,55,0.85) 0%, rgba(63,90,42,0.55) 40%, rgba(40,40,30,0) 72%);
  }

  .heavy { font-family: "Archivo Black", "Arial Black", sans-serif; }
  .lime { color: var(--lime); }

  /* back cover */
  .back-headline {
    position: absolute; left: 0; right: 0; top: 36px; text-align: center;
    font-size: 30px; line-height: 1; color: var(--white); white-space: nowrap;
  }
  .back-copy {
    position: absolute; left: 44px; width: 424px;
    font-family: "Arimo", Arial, sans-serif; font-weight: 700;
    text-transform: uppercase; color: var(--white);
  }
  .back-copy--lead { top: 110px; left: 50px; width: 410px; font-size: 9.2px; line-height: 13px; text-align: center; }
  .back-copy--body { font-size: 10px; line-height: 16.2px; text-align: justify; }
  .back-copy--p1 { top: 193px; }
  .back-copy--p2 { top: 319px; }
  .back-copy--p3 { top: 416px; }

  .author-photo {
    position: absolute; left: 41px; top: 507px; width: 85px; height: 120px;
    background: var(--paper); border: 3px solid var(--lime);
  }
  .author-bio {
    position: absolute; left: 134px; top: 523px; width: 340px;
    font-family: "Arimo", Arial, sans-serif; font-weight: 700; text-transform: uppercase;
    font-size: 10px; line-height: 16.2px; color: var(--white); text-align: justify;
  }
  .publisher-box {
    position: absolute; left: 318px; top: 637px; width: 170px; height: 99px;
    background: var(--paper); border: 3px solid var(--lime);
  }

  /* spine */
  .spine-title {
    position: absolute; left: 0; top: 36px; width: 64px; height: 440px;
    writing-mode: vertical-rl; display: flex; align-items: center;
    font-size: 29px; line-height: 64px; color: var(--white); white-space: nowrap;
  }
  .spine-band { position: absolute; left: 0; bottom: 0; width: 64px; height: 236px; background: var(--lime); }
  .spine-author {
    position: absolute; left: 0; top: 34px; width: 64px; height: 180px;
    writing-mode: vertical-rl; display: flex; align-items: center;
    font-size: 14px; line-height: 64px; color: var(--ink); white-space: nowrap;
  }

  /* front cover */
  .title-block { position: absolute; left: 0; right: 0; top: 36px; text-align: center; color: var(--white); }
  .title-line { display: block; }
  .title-small { font-family: "Arimo", Arial, sans-serif; font-weight: 400; font-size: 29px; line-height: 1.1; text-shadow: 1px 1px 2px rgba(0,0,0,0.7); }
  .title-large { font-size: 34px; line-height: 1.15; text-shadow: 2px 2px 2px rgba(0,0,0,0.8); margin: 2px 0 4px; }
  .title-hero { font-size: 46px; line-height: 1.05; color: var(--lime); text-shadow: 2px 2px 0 rgba(0,0,0,0.85); }
  .subtitle {
    position: absolute; left: 0; right: 0; top: 218px; text-align: center;
    font-family: "Arimo", Arial, sans-serif; font-weight: 700; text-transform: uppercase;
    font-size: 13px; line-height: 16px; color: var(--white); text-shadow: 1px 1px 2px rgba(0,0,0,0.9);
  }
  .front-author { position: absolute; left: 0; right: 0; top: 718px; text-align: center; font-size: 20px; letter-spacing: 0.5px; }
</style>
</head>
<body>
<main class="jacket">

  <section class="back-cover">
    <div class="scene" role="img" aria-label="Dark stormy sky over a cracked, barren desert floor in greyscale"></div>
    <h2 class="back-headline heavy"><span class="lime">ARRANGE YOUR</span> SPACES</h2>
    <p class="back-copy back-copy--lead">Lorem ipsum dolor sit amet, consectetuer adipiscing elit. Aenean commodo ligula eget dolor. Aenean massa. Cum sociis natoque penatibus et magnis dis parturient montes, nascetur ridiculus mus. Donec quam felis, ultricies nec, pellentesque eu, pretium quis, sem. Nulla consequat massa quis enim. Donec pede justo, fringilla vel, aliquet nec,</p>
    <p class="back-copy back-copy--body back-copy--p1">Vulputate eget, arcu. In enim justo, rhoncus ut, imperdiet a, venenatis vitae, justo. Nullam dictum felis eu pede mollis pretium. Integer tincidunt. Cras dapibus. Vivamus elementum semper nisi. Aenean vulputate eleifend tellus. Aenean leo ligula, porttitor eu, consequat vitae, eleifend ac, enim. Aliquam lorem ante, dapibus in, viverra quis, feugiat a, tellus. Phasellus viverra nulla ut metus varius laoreet. Quisque rutrum. Aenean</p>
    <p class="back-copy back-copy--body back-copy--p2">Imperdiet. Etiam ultricies nisi vel augue. Curabitur ullamcorper ultricies nisi. Nam eget dui. Etiam rhoncus. Maecenas tempus, tellus eget condimentum rhoncus, sem quam semper libero, sit amet adipiscing sem neque sed ipsum. Nam quam nunc, blandit vel, luctus pulvinar, hendrerit id, lorem. Maecenas nec odio et ante tincidunt tempus. Donec</p>
    <p class="back-copy back-copy--body back-copy--p3">Vitae sapien ut libero venenatis faucibus. Nullam quis ante. Etiam sit amet orci eget eros faucibus tincidunt. Duis leo. Sed fringilla mauris sit amet nibh. Donec sodales sagittis magna. Sed consequat, leo eget bibendum sodales, augue velit cursus nunc,</p>
    <div class="author-photo" role="img" aria-label="Author portrait placeholder"></div>
    <p class="author-bio"><span class="lime">Dr. Miriam Okafor</span> vitae sapien ut libero venenatis faucibus. Nullam quis ante. Etiam sit amet orci eget eros faucibus tincidunt. Duis leo. Sed fringilla mauris sit amet nibh. Donec sodales sagittis magna. Sed consequat, leo eget bibendum sodales, augue velit cursus nunc,</p>
    <div class="publisher-box"></div>
  </section>

  <section class="spine">
    <div class="scene" role="img" aria-label="Stormy sky and cracked desert continuing across the spine"></div>
    <div class="spine-title heavy"><span class="lime">ARRANGE YOUR&nbsp;</span>SPACES</div>
    <div class="spine-band">
      <div class="spine-author heavy">DR. MIRIAM OKAFOR</div>
    </div>
  </section>

  <section class="front-cover">
    <div class="scene scene--front" role="img" aria-label="Cracked dark desert under a stormy sky, with a brain made of green leaves and a pink nervous system of roots emerging from the ground"></div>
    <h1 class="title-block">
      <span class="title-line title-small">UNDER</span>
      <span class="title-line title-large heavy">COPPER LANTERNS</span>
      <span class="title-line title-small">TO</span>
      <span class="title-line title-hero heavy">WANDERLAND</span>
    </h1>
    <p class="subtitle">Practical notes on arranging your<br>garden, kitchen, and study</p>
    <p class="front-author heavy lime">DR. MIRIAM OKAFOR</p>
  </section>

</main>
</body>
</html>
```